Patent Law

Need to develop a home page for a patent lawyer.

Colors should go with logo, blues...

Company Name- Corvel Tindry, PLLC

Company Overview-

I am an Intellectual Property Lawyer and focus on patents, copyrights, trademarks, & trade secrets. I work with small businesses and start ups in the chemical and biotech industries.

Why Us-

I am small firm that can provide large-firm service at a reasonable price. I also can charge flat-fees for entreprenuers in certain practice areas.

Services-
Intellectual Property
Patents
Copyrights
Trademarks
Trade secrets
Healthcare Compliance
Elder law
Wills
Trusts

Website we like-
http://www.quarnlowtide.example/ - within industry!!
http://www.vopperhask.example/
http://dulbrickovan.example/
http://thefernwoldguides.example/

Target Market(s)

My customers will be small business, specifically small start-up companies in the chemical and biotech arena.

Industry/Entity Type

Trade

Requirements
Must have
• Colors should go with logo, blues...

```html
<!DOCTYPE html>
<html lang="en">
<head>
<meta charset="utf-8">
<title>Corvel Tindry, PLLC – Patent Expertise</title>
<link rel="stylesheet" href="https://fonts.googleapis.com/css2?family=Cinzel:wght@400;600&family=Figtree:wght@400;500;600&display=swap">
<style>
:root{
  --navy:#0b3a9a;
  --blue:#1565c0;
  --blue-bright:#0a6ad0;
  --sky:#7fa6f0;
  --green:#6f9a0a;
  --green-dark:#5d8406;
  --ink:#444;
  --muted:#666;
  --paper:#efefef;
  --card:#ffffff;
  --rule:#e2e2e2;
  --dark:#232323;
  --dark-2:#2e2e2e;
  --white:#fff;
}
*{box-sizing:border-box;margin:0;padding:0}
html,body{width:1108px;height:1200px;overflow:hidden}
body{font-family:"Figtree",sans-serif;color:var(--ink);background:var(--paper)}
.page{position:relative;width:1108px;height:1200px;overflow:hidden;background:var(--paper)}
.abs{position:absolute}

/* header */
.site-header{position:absolute;left:0;top:0;width:1108px;height:95px;background:linear-gradient(#fff,#ececec);border-top:2px solid var(--dark)}
.brand{left:143px;top:38px;display:flex;align-items:center;gap:8px;font-family:"Cinzel",serif;font-weight:600;font-size:15px;color:var(--navy)}
.brand-mark{width:14px;height:14px;border-radius:50%;background:var(--blue)}
.utility{left:807px;top:0;width:158px;height:28px;background:var(--dark);display:flex;align-items:center;font-size:11px;font-weight:600;color:var(--white)}
.utility .phone{display:flex;align-items:center;gap:7px;padding:0 10px 0 12px;border-right:1px solid #555;height:18px}
.utility .map{padding-left:12px}
.main-nav{left:448px;top:44px;display:flex;align-items:center;font-family:"Cinzel",serif;font-size:12.5px;color:#666}
.main-nav a{color:inherit;text-decoration:none;padding:0 12px;border-left:1px dotted #bbb;line-height:12px}
.main-nav a:nth-child(2){border-left:none}
.main-nav a.active{background:var(--blue-bright);color:var(--white);padding:6px 11px;line-height:12px;border:none}

/* hero */
.hero{position:absolute;left:0;top:95px;width:1108px;height:388px;background:radial-gradient(ellipse at 70% 40%,#1a55c2 0%,#0d3e9e 55%,#082f85 100%);overflow:hidden}
.hero-portrait{position:absolute;left:636px;top:-14px;width:310px;height:402px;background:linear-gradient(180deg,#3a5ca8 0%,#24335c 45%,#1b2236 100%);border-radius:120px 120px 0 0;opacity:.85}
.hero-title{left:143px;top:80px;font-family:"Cinzel",serif;font-weight:600;font-size:42px;color:var(--white);letter-spacing:.5px}
.hero-sub{left:143px;top:134px;font-size:33px;color:var(--sky);letter-spacing:2px;font-weight:400}
.hero-copy{left:143px;top:184px;width:440px;font-size:12.5px;line-height:19.5px;color:var(--white)}
.btn-hero{left:143px;top:258px;width:134px;height:33px;background:var(--green);color:var(--white);font-size:12.5px;font-weight:600;display:flex;align-items:center;justify-content:center;gap:10px}
.dots{left:531px;top:355px;display:flex;gap:3px}
.dots span{width:11px;height:11px;border-radius:50%;background:var(--white)}
.dots span.ring{background:var(--blue);border:3px solid var(--white)}

/* about */
.about-title{left:0;top:536px;width:1108px;text-align:center;font-family:"Cinzel",serif;font-size:32px;color:var(--navy)}
.about-copy{left:165px;top:581px;width:778px;text-align:center;font-size:12.5px;line-height:19.5px;color:#555}

/* cards */
.card{position:absolute;top:688px;width:248px;height:348px;background:var(--card);border:1px solid #ddd;border-bottom:3px solid #d6d6d6;overflow:hidden}
.card-media{position:relative;width:100%}
.card-media .label{position:absolute;left:16px;font-family:"Cinzel",serif;font-size:18px;color:var(--white)}
.why{left:143px}
.why .card-media{height:163px;background:radial-gradient(circle at 45% 55%,#6fc4e0 0%,#2f7fa8 35%,#12364f 75%,#0d2a3f 100%)}
.why .label{top:128px}
.why h3{position:absolute;left:20px;top:177px;font-size:14px;font-weight:600;color:var(--blue)}
.why p{position:absolute;left:20px;top:203px;width:210px;font-size:10.6px;line-height:14.7px;color:#555}
.btn-small{position:absolute;height:22px;font-size:10.5px;font-weight:600;color:var(--white);display:flex;align-items:center;justify-content:center;gap:6px}
.why .btn-small{left:20px;top:308px;width:99px;background:var(--blue-bright)}
.do{left:430px}
.do .card-media{height:116px;background:linear-gradient(120deg,#8a8f98 0%,#c7c9cd 40%,#6b6e75 70%,#3d3f44 100%)}
.do .label{top:82px}
.services{position:absolute;left:20px;top:128px;width:214px;list-style:none}
.services li{height:24.4px;display:flex;align-items:center;gap:7px;font-size:11px;color:var(--muted);border-bottom:1px solid var(--rule)}
.services li:last-child{border-bottom:none}
.services li.current{color:var(--blue)}
.contact{left:717px}
.contact .card-media{height:163px;background:linear-gradient(135deg,#eeeee8 0%,#e4e6dc 50%,#d9ddd0 100%)}
.contact .label{top:127px;color:var(--navy)}
.contact h3{position:absolute;left:30px;top:184px;font-size:14px;font-weight:600;color:var(--blue)}
.contact-row{position:absolute;left:20px;width:216px;display:flex;gap:8px;color:var(--muted);font-size:11px;line-height:14px}
.contact-row.addr{top:214px;border-bottom:1px solid var(--rule);padding-bottom:5px}
.contact-row.tel{top:242px;font-size:16px;line-height:22px;border-bottom:1px solid var(--rule);padding-bottom:4px;align-items:center}
.contact-row.mail{top:273px;align-items:center}
.contact .btn-small{left:30px;top:307px;width:99px;background:var(--green)}

/* footer */
.site-footer{position:absolute;left:0;top:1092px;width:1108px;height:108px;background:var(--dark)}
.foot-nav{left:143px;top:37px;display:flex;font-size:10.5px;color:#bbb}
.foot-nav a{color:inherit;text-decoration:none;padding:0 8px;border-left:1px dotted #666}
.foot-nav a:first-child{padding-left:0;border-left:none;color:var(--white)}
.follow{left:811px;top:33px;display:flex;align-items:center;gap:4px;font-size:10.5px;color:#bbb}
.follow span.t{margin-right:4px}
.soc{width:20px;height:20px}
.s1{background:#3b5a9a}.s2{background:#2ba6e1}.s3{background:#1a7bb5}.s4{background:#c9362b}
.foot-rule{left:143px;top:70px;width:822px;height:1px;background:#3a3a3a}
.copyright{left:0;top:82px;width:1108px;text-align:center;font-size:10px;color:#bbb}
</style>
</head>
<body>
<div class="page">

  <header class="site-header">
    <div class="abs brand"><span class="brand-mark"></span>Corvel Tindry, PLLC</div>
    <div class="abs utility">
      <span class="phone">
        <svg width="16" height="16" viewBox="0 0 16 16"><circle cx="8" cy="8" r="7.5" fill="none" stroke="#888"/><path d="M5.5 4.5l1.5 0 .7 2-1 .8a5 5 0 0 0 2 2l.8-1 2 .7v1.5c-3 .6-6.6-3-6-6z" fill="#fff"/></svg>
        877-5550142
      </span>
      <span class="map">MAP</span>
    </div>
    <nav class="abs main-nav">
      <a class="active">HOME</a><a>FIRM</a><a>PEOPLE</a><a>PRACTICES</a><a>LIBRARY</a><a>NEWS</a><a>CONTACT US</a>
    </nav>
  </header>

  <section class="hero">
    <div class="hero-portrait" role="img" aria-label="Portrait of a senior attorney in a dark suit with arms folded"></div>
    <h1 class="abs hero-title">CORVEL TINDRY, PLLC</h1>
    <div class="abs hero-sub">PATENT EXPERTISE</div>
    <p class="abs hero-copy">Lorem Ipsum is simply dummy text of the printing and typesetting industry. Lorem Ipsum has been the industry's standard when an unknown printer took a galley of type and scrambled it to make a type specimen book.</p>
    <a class="abs btn-hero">READ MORE
      <svg width="16" height="8" viewBox="0 0 16 8"><path d="M0 4h14M11 1l3 3-3 3" stroke="#fff" fill="none"/></svg>
    </a>
    <div class="abs dots"><span></span><span class="ring"></span><span></span></div>
  </section>

  <h2 class="abs about-title">About Corvel Tindry, PLLC</h2>
  <p class="abs about-copy">Lorem Ipsum is simply dummy text of the printing and typesetting industry. Lorem Ipsum has been the industry's standard dummy text ever since the 1500s, when an unknown printer took a galley of type and scrambled it to make a type specimen book. It has survived not only five centuries, but also the leap into electronic typesetting, remaining essentially unchanged.</p>

  <article class="card why">
    <div class="card-media" role="img" aria-label="Abstract blurred blue swirl background"><span class="label">WHY US</span></div>
    <h3>What Makes us different?</h3>
    <p>Lorem Ipsum is simply dummy text of the printing and typesetting industry. Lorem Ipsum has been the industry's standard dummy text ever since the when an unknown printer took a galley of type and scrambled it to specimen book.</p>
    <a class="btn-small">READ MORE
      <svg width="14" height="8" viewBox="0 0 14 8"><path d="M0 4h12M9 1l3 3-3 3" stroke="#fff" fill="none"/></svg>
    </a>
  </article>

  <article class="card do">
    <div class="card-media" role="img" aria-label="Blurred photo of two lawyers reviewing documents"><span class="label">WHAT WE DO?</span></div>
    <ul class="services">
      <li><svg width="14" height="14" viewBox="0 0 14 14"><rect x=".5" y=".5" width="13" height="13" fill="none" stroke="#999" stroke-dasharray="2 1"/><path d="M3.5 7l2.5 2.5 5-5.5" stroke="#555" fill="none" stroke-width="1.4"/></svg>Intellectual Property</li>
      <li><svg width="14" height="14" viewBox="0 0 14 14"><rect x=".5" y=".5" width="13" height="13" fill="none" stroke="#999" stroke-dasharray="2 1"/><path d="M3.5 7l2.5 2.5 5-5.5" stroke="#555" fill="none" stroke-width="1.4"/></svg>Patents</li>
      <li><svg width="14" height="14" viewBox="0 0 14 14"><rect x=".5" y=".5" width="13" height="13" fill="none" stroke="#999" stroke-dasharray="2 1"/><path d="M3.5 7l2.5 2.5 5-5.5" stroke="#555" fill="none" stroke-width="1.4"/></svg>Copyrights</li>
      <li class="current"><svg width="14" height="14" viewBox="0 0 14 14"><rect x=".5" y=".5" width="13" height="13" fill="none" stroke="#1565c0" stroke-dasharray="2 1"/><path d="M3.5 7l2.5 2.5 5-5.5" stroke="#1565c0" fill="none" stroke-width="1.4"/></svg>Trademarks</li>
      <li><svg width="14" height="14" viewBox="0 0 14 14"><rect x=".5" y=".5" width="13" height="13" fill="none" stroke="#999" stroke-dasharray="2 1"/><path d="M3.5 7l2.5 2.5 5-5.5" stroke="#555" fill="none" stroke-width="1.4"/></svg>Trade secrets</li>
      <li><svg width="14" height="14" viewBox="0 0 14 14"><rect x=".5" y=".5" width="13" height="13" fill="none" stroke="#999" stroke-dasharray="2 1"/><path d="M3.5 7l2.5 2.5 5-5.5" stroke="#555" fill="none" stroke-width="1.4"/></svg>Healthcare Compliance</li>
      <li><svg width="14" height="14" viewBox="0 0 14 14"><rect x=".5" y=".5" width="13" height="13" fill="none" stroke="#999" stroke-dasharray="2 1"/><path d="M3.5 7l2.5 2.5 5-5.5" stroke="#555" fill="none" stroke-width="1.4"/></svg>Elder law</li>
      <li><svg width="14" height="14" viewBox="0 0 14 14"><rect x=".5" y=".5" width="13" height="13" fill="none" stroke="#999" stroke-dasharray="2 1"/><path d="M3.5 7l2.5 2.5 5-5.5" stroke="#555" fill="none" stroke-width="1.4"/></svg>Wills</li>
    </ul>
  </article>

  <article class="card contact">
    <div class="card-media" role="img" aria-label="Street map showing the office location"><span class="label">GET IN TOUCH</span></div>
    <h3>Corvel Tindry, PLLC</h3>
    <div class="contact-row addr">
      <svg width="12" height="16" viewBox="0 0 12 16"><path d="M6 0a6 6 0 0 0-6 6c0 4 6 10 6 10s6-6 6-10a6 6 0 0 0-6-6z" fill="#888"/><circle cx="6" cy="6" r="2.2" fill="#fff"/></svg>
      <span>Larkfield Commons<br>Tessbury, FL 33000</span>
    </div>
    <div class="contact-row tel">
      <svg width="12" height="16" viewBox="0 0 12 16"><rect x="1.5" y=".5" width="9" height="15" rx="1.5" fill="none" stroke="#777" stroke-width="1.4"/><rect x="3.5" y="2.5" width="5" height="9" fill="#777"/></svg>
      +877 5550142
    </div>
    <div class="contact-row mail">
      <svg width="14" height="10" viewBox="0 0 14 10"><rect x=".5" y=".5" width="13" height="9" fill="#999"/><path d="M.5.5l6.5 5 6.5-5" stroke="#fff" fill="none"/></svg>
      info@corveltindry.example
    </div>
    <a class="btn-small">
      <svg width="12" height="12" viewBox="0 0 12 12"><circle cx="6" cy="3.5" r="3" fill="#fff"/><path d="M0 12c0-4 3-5.5 6-5.5s6 1.5 6 5.5z" fill="#fff"/></svg>
      CONTACT US
    </a>
  </article>

  <footer class="site-footer">
    <nav class="abs foot-nav"><a>Home</a><a>Firm</a><a>People</a><a>Practices</a><a>Library</a><a>News</a><a>Contact Us</a></nav>
    <div class="abs follow"><span class="t">Follow us on</span><span class="soc s1"></span><span class="soc s2"></span><span class="soc s3"></span><span class="soc s4"></span></div>
    <div class="abs foot-rule"></div>
    <p class="abs copyright">Copyright © 2013, Corvel Tindry, PLLC. All rights reserverd.</p>
  </footer>

</div>
</body>
</html>
```